The Bright Lantern, an online college fair for non-traditional students, needs a web site

I need design and coding for a functioning web site that will serve as an online college fair that connects non-traditional students with college admissions officers and college advisors. I have chosen Wordpress and the "Meridian" theme for the site, and you can see what I already have here: https://brightlanternhub.example/
I need help setting up the site's pages and functionality, including SEO optimization and a password protected area. I will manage all content. In addition to me as the administrator, other users will be: college admissions officers, non-traditional students (like homeschoolers), and college advisors.
Target Market(s)
Homeschoolers and college/university admissions officers
Industry/Entity Type
College
Coding
Coded - Design and coding required
Number of Pages Required
5+ page
Font styles to use
Requirements
Must have
- - An inviting but professional look (see the logo as a starting point)
- - Easy to navigate
- - A way to register subscribed members (students)
- - A password-protected "members only" area
- - Virtual "booths" on the Schools page that lead to a detail page for each school
- - SEO optimized
Nice to have
- - Searchable site

```html
<!DOCTYPE html>
<html lang="en">
<head>
<meta charset="utf-8">
<title>The Bright Lantern – Online College Fair</title>
<link href="https://fonts.googleapis.com/css2?family=Montserrat:wght@400;500;600;700&family=Oswald:wght@400;500&display=swap" rel="stylesheet">
<style>
:root{
  --ink:#222428;
  --slate:#3b4650;
  --slate-dark:#2a2d33;
  --footer:#25272c;
  --footer-deep:#1b1c20;
  --red:#d0202a;
  --panel:#f0f0f0;
  --line:#c9c9c9;
  --muted:#6d6d6d;
  --white:#ffffff;
}
*{box-sizing:border-box;margin:0;padding:0}
html,body{width:1200px;height:5158px;overflow:hidden}
body{position:relative;background:var(--white);color:var(--ink);font-family:"Montserrat",Arial,sans-serif}
.abs{position:absolute}
.fill{position:absolute}
.title{font-family:"Oswald","Arial Narrow",sans-serif;font-weight:400;text-transform:uppercase;text-align:center;letter-spacing:1px;font-size:27px;color:var(--ink)}

/* header */
.topbar{left:0;top:0;width:1200px;height:145px}
.contact-mini{top:52px;font-size:12px;line-height:17px;color:var(--muted);display:flex;gap:10px;align-items:flex-start}
.brand{left:448px;top:36px;display:flex;align-items:center;gap:12px}
.brand-mark{width:58px;height:58px;background:var(--red)}
.brand-name{font-weight:600;font-size:24px;color:var(--ink);text-transform:uppercase;letter-spacing:1px;line-height:1}
.mainnav{left:0;top:146px;width:1200px;height:44px;border-top:1px solid var(--line)}
.mainnav ul{list-style:none;display:flex;gap:28px;position:absolute;left:86px;top:13px;font-size:13px;color:var(--ink)}
.btn{position:absolute;top:6px;height:32px;background:var(--slate);color:var(--white);font-size:14px;font-weight:600;letter-spacing:1px;display:flex;align-items:center;justify-content:center}

/* hero */
.hero{left:0;top:190px;width:1200px;height:532px;background:linear-gradient(100deg,#5b4a3c 0%,#8a6f58 35%,#6e5a4b 65%,#4c3f35 100%)}
.hero-shade{position:absolute;inset:0;background:rgba(20,20,25,.35)}
.hero h1{position:absolute;left:0;width:1200px;top:125px;text-align:center;color:var(--white);font-size:46px;font-weight:600;letter-spacing:4px}
.hero p{position:absolute;left:400px;width:400px;top:186px;text-align:center;color:var(--white);font-size:13px;line-height:17px}
.search{position:absolute;left:327px;top:336px;width:447px;height:58px;background:rgba(40,40,45,.7);color:#ddd;font-size:15px;padding:19px 18px}
.search-btn{position:absolute;left:784px;top:336px;width:179px;height:58px;background:var(--white);color:var(--red);font-size:16px;display:flex;align-items:center;justify-content:center}

/* how it works */
.service{width:480px;height:222px;background:var(--panel);border:1px solid #999;box-shadow:5px 5px 0 var(--slate-dark)}
.service svg{position:absolute;left:40px;top:70px}
.service .divider{position:absolute;left:150px;top:55px;width:2px;height:110px;background:var(--ink)}
.service h3{position:absolute;left:190px;top:56px;font-size:28px;font-weight:600;text-transform:uppercase;line-height:32px}
.service p{position:absolute;left:190px;width:260px;font-size:12px;line-height:16px;color:var(--ink)}

/* advisors */
.rule{left:86px;top:1324px;width:1028px;height:2px;background:var(--line)}
.advisor{top:1428px;width:327px;height:361px;background:linear-gradient(180deg,#e9ecef,#c7ccd1)}
.advisor .plate{position:absolute;left:0;top:251px;width:272px;height:69px;background:var(--slate);color:var(--white);padding:10px 20px}
.plate strong{display:block;font-family:"Oswald",sans-serif;font-weight:400;font-size:26px;line-height:28px;text-transform:uppercase}
.plate span{font-size:11px;text-transform:uppercase;letter-spacing:1px}

/* students */
.band{left:0;top:1902px;width:1200px;height:196px;background:var(--slate)}
.photo{position:absolute}

/* featured school */
.school-photo{left:0;top:2718px;width:592px;height:670px;background:linear-gradient(180deg,#3f7fd0 0%,#8fb8e6 45%,#6b6f5e 60%,#4e7d2f 85%,#3f6b26 100%)}
.school-panel{left:592px;top:2718px;width:608px;height:670px;background:#f3f3f3}
.feature{position:absolute;top:140px;width:170px;text-align:center}
.feature .icon{width:62px;height:62px;margin:0 auto;border-radius:50%;background:var(--white);border:1px solid var(--line);display:flex;align-items:center;justify-content:center}
.feature h4{font-size:12px;font-weight:600;text-transform:uppercase;margin-top:22px;text-align:left}
.feature p{font-size:11.5px;line-height:16px;color:var(--ink);margin-top:6px;text-align:left}
.feature em{display:block;text-align:center;font-size:11px;margin-top:4px}

/* news */
.news{width:236px;text-align:left}
.news.right{text-align:right}
.news .date{font-size:14px;font-weight:500}
.news .date b{font-size:44px;font-weight:500;margin-left:4px}
.news p{font-size:11px;line-height:14px;text-transform:uppercase;margin-top:6px}
.news .meta{font-size:10px;color:var(--muted);margin-top:8px}
.news .meta i{color:var(--red);font-style:normal}
.news .more{font-size:12px;font-weight:700;color:var(--red);margin-top:10px}

/* newsletter */
.newsletter{left:0;top:3973px;width:1200px;height:344px;background:linear-gradient(90deg,#26262a,#3a3634 50%,#26262a)}
.newsletter .shade{position:absolute;inset:0;background:rgba(0,0,0,.4)}
.email-field{position:absolute;left:320px;top:186px;width:370px;height:44px;border:2px solid var(--white);color:var(--white);font-size:16px;padding:10px 14px}
.subscribe{position:absolute;left:703px;top:186px;width:183px;height:44px;background:var(--white);color:var(--ink);font-size:17px;font-weight:600;display:flex;align-items:center;justify-content:center}

/* contact */
.message{left:0;top:4352px;width:378px;height:481px;background:var(--slate-dark);color:var(--white);padding:90px 86px 0 86px}
.eyebrow{font-size:12px;font-weight:600;text-transform:uppercase;letter-spacing:1px}
.message h2,.info h2{font-family:"Oswald",sans-serif;font-weight:400;font-size:24px;text-transform:uppercase;letter-spacing:1px;margin-top:8px}
.field{margin-top:42px;font-size:10px;font-weight:600;text-transform:uppercase;border-bottom:1px solid #888;padding-bottom:14px}
.info{left:405px;top:4352px;width:360px;height:481px;padding-top:90px}
.info-item{display:flex;gap:16px;margin-top:40px;align-items:flex-start}
.info-item b{display:block;font-size:12px;font-weight:600;text-transform:uppercase}
.info-item span{font-size:10px;text-transform:uppercase}
.map{left:777px;top:4352px;width:423px;height:481px;background:linear-gradient(135deg,#ece9e1,#dcd7cb 50%,#cfe0c2)}

/* footer */
.footer{left:0;top:4850px;width:1200px;height:276px;background:var(--footer);color:var(--white)}
.col{position:absolute;top:38px;font-size:11px;line-height:15px;text-transform:uppercase}
.col h5{font-size:13px;font-weight:700;margin-bottom:10px}
.col ul{list-style:none}
.social li{display:flex;align-items:center;gap:10px;margin-bottom:8px}
.social i{width:14px;height:14px;border-radius:50%;background:var(--white);display:inline-block}
.copyright{left:0;top:5126px;width:1200px;height:32px;background:var(--footer-deep);color:var(--white);font-size:11px;text-align:center;line-height:32px;letter-spacing:1px}
</style>
</head>
<body>

<header class="abs topbar">
  <div class="abs contact-mini" style="left:86px">
    <svg width="18" height="24" viewBox="0 0 18 24"><path d="M9 1C4.6 1 1 4.5 1 8.9 1 15 9 23 9 23s8-8 8-14.1C17 4.5 13.4 1 9 1z" fill="none" stroke="#555" stroke-width="2"/><circle cx="9" cy="9" r="3" fill="#555"/></svg>
    <div>Larchwood 4/12,<br>Old Town Centre</div>
  </div>
  <div class="abs brand">
    <div class="brand-mark"></div>
    <div class="brand-name">The Bright Lantern</div>
  </div>
  <div class="abs contact-mini" style="left:985px">
    <svg width="18" height="24" viewBox="0 0 18 24"><rect x="3" y="1" width="12" height="22" rx="2" fill="none" stroke="#555" stroke-width="2"/><circle cx="9" cy="19" r="1.5" fill="#555"/></svg>
    <div>0123 456 7890<br>0123 456 7891</div>
  </div>
</header>

<nav class="abs mainnav">
  <ul><li>Home</li><li>students</li><li>school</li><li>advisors</li><li>Member Resources</li><li>News</li><li>Contact Us</li></ul>
  <div class="btn" style="left:858px;width:118px">SIGN UP</div>
  <div class="btn" style="left:1010px;width:114px">LOG IN</div>
</nav>

<section class="abs hero" role="img" aria-label="Photo of smiling students gathered in a library">
  <div class="hero-shade"></div>
  <h1>BEST EDUCATION FIRM</h1>
  <p>It is a long established fact that a reader will be distracted by the readable content of a page when looking at its layout. The point of</p>
  <div class="search">Search Colleges,Schools</div>
  <div class="search-btn">Search</div>
</section>

<h2 class="abs title" style="left:0;top:748px;width:1200px">How it Works</h2>
<div class="abs rule" style="top:790px;left:510px;width:180px;height:1px"></div>

<article class="abs service" style="left:86px;top:826px">
  <svg width="80" height="70" viewBox="0 0 80 70"><rect x="4" y="44" width="10" height="22" fill="#222"/><rect x="20" y="34" width="10" height="32" fill="#222"/><rect x="36" y="40" width="10" height="26" fill="#222"/><rect x="52" y="24" width="10" height="42" fill="#222"/><path d="M6 30 24 16 40 24 66 4" fill="none" stroke="#222" stroke-width="4"/><path d="M58 2h10v10" fill="none" stroke="#222" stroke-width="4"/></svg>
  <div class="divider"></div>
  <h3>Business</h3>
  <p style="top:96px">Business Trends changing with latest courses are available with us.</p>
</article>
<article class="abs service" style="left:630px;top:826px">
  <svg width="80" height="70" viewBox="0 0 80 70"><rect x="4" y="48" width="10" height="18" fill="#222"/><rect x="20" y="40" width="10" height="26" fill="#222"/><rect x="36" y="30" width="10" height="36" fill="#222"/><rect x="52" y="20" width="10" height="46" fill="#222"/><path d="M4 36 30 22 44 28 70 6" fill="none" stroke="#222" stroke-width="4"/><path d="M60 4h12v12" fill="none" stroke="#222" stroke-width="4"/></svg>
  <div class="divider"></div>
  <h3>Accounting</h3>
  <p style="top:96px">Accounting need to be perfect. Come and join with us with best resources.</p>
</article>
<article class="abs service" style="left:86px;top:1066px">
  <svg width="80" height="70" viewBox="0 0 80 70"><path d="M14 4c30 20 30 42 52 62M66 4C36 24 36 46 14 66" fill="none" stroke="#222" stroke-width="5"/><path d="M24 16h32M30 28h20M30 42h20M24 54h32" stroke="#222" stroke-width="3"/></svg>
  <div class="divider"></div>
  <h3>Science &amp;<br>Technology</h3>
  <p style="top:128px">Latest technologies online courses are available with new courses.</p>
</article>
<article class="abs service" style="left:630px;top:1066px">
  <svg width="80" height="70" viewBox="0 0 80 70"><circle cx="22" cy="8" r="6" fill="#222"/><circle cx="56" cy="8" r="6" fill="#222"/><path d="M22 16v24l-8 26M22 40l8 26M56 16v24l-8 26M56 40l8 26M22 24l14 10 20-10" fill="none" stroke="#222" stroke-width="6" stroke-linecap="round"/></svg>
  <div class="divider"></div>
  <h3>Creative Arts<br>&amp; Med</h3>
  <p style="top:128px">Come and explore your creative arts and make by going further.</p>
</article>

<div class="abs rule"></div>
<h2 class="abs title" style="left:0;top:1347px;width:1200px">Featured Advisors</h2>

<figure class="abs advisor" style="left:86px" role="img" aria-label="Portrait photo of advisor Mara Ellison">
  <figcaption class="plate"><strong>Mara Ellison</strong><span>Designing Staff</span></figcaption>
</figure>
<figure class="abs advisor" style="left:447px" role="img" aria-label="Portrait photo of advisor Theo Barrett">
  <figcaption class="plate"><strong>Theo Barrett</strong><span>Project Manager</span></figcaption>
</figure>
<figure class="abs advisor" style="left:808px" role="img" aria-label="Portrait photo of advisor Calvin Shore">
  <figcaption class="plate"><strong>Calvin Shore</strong><span>Designing Staff</span></figcaption>
</figure>

<section class="abs band">
  <h2 class="title" style="color:#fff;margin-top:38px">Students</h2>
</section>
<div class="photo" style="left:86px;top:2019px;width:578px;height:458px;background:linear-gradient(135deg,#8a7a63,#b29b7c 50%,#7c8a5a)" role="img" aria-label="Photo of a student with a backpack outside a campus building"></div>
<div class="photo" style="left:695px;top:2019px;width:413px;height:331px;background:linear-gradient(135deg,#b9a7c9,#d8cfe0 50%,#a48bb5)" role="img" aria-label="Photo of a student holding books"></div>
<div class="photo" style="left:86px;top:2494px;width:578px;height:206px;background:linear-gradient(90deg,#b8744a,#d7a989 50%,#f0e6dc)" role="img" aria-label="Photo of a smiling student"></div>
<div class="photo" style="left:695px;top:2367px;width:413px;height:333px;background:linear-gradient(135deg,#9b5a3a,#c9865f 50%,#2f9bb0)" role="img" aria-label="Photo of a student with glasses"></div>

<div class="abs school-photo" role="img" aria-label="Photo of a historic college tower on a green lawn"></div>
<section class="abs school-panel">
  <h2 class="title" style="margin-top:58px">Featured School</h2>
  <div class="abs rule" style="left:224px;top:110px;width:160px;height:1px"></div>
  <div class="feature" style="left:44px">
    <div class="icon"><svg width="28" height="28" viewBox="0 0 28 28"><rect x="4" y="5" width="20" height="5" fill="#222"/><rect x="6" y="12" width="18" height="5" fill="#222"/><rect x="3" y="19" width="21" height="5" fill="#222"/></svg></div>
    <h4>Books &amp; Library</h4>
    <p>It is a long established fact that a reader will be distracted by the readable content of a page when looking at its layout. The point of</p>
    <em>view more</em>
  </div>
  <div class="feature" style="left:219px">
    <div class="icon"><svg width="28" height="28" viewBox="0 0 28 28"><path d="M20 3l5 5L10 23l-6 1 1-6z" fill="none" stroke="#222" stroke-width="2.5"/></svg></div>
    <h4>Learn Courses</h4>
    <p>It is a long established fact that a reader will be distracted by the readable content of a page when looking at its layout. The point of</p>
    <em>view more</em>
  </div>
  <div class="feature" style="left:394px">
    <div class="icon"><svg width="28" height="28" viewBox="0 0 28 28"><path d="M4 14l7 7L24 7" fill="none" stroke="#222" stroke-width="3"/></svg></div>
    <h4>Become a Good..</h4>
    <p>It is a long established fact that a reader will be distracted by the readable content of a page when looking at its layout. The point of</p>
    <em>view more</em>
  </div>
  <div class="photo" style="left:44px;top:474px;width:499px;height:162px;background:linear-gradient(90deg,#6c625a,#a08c78 50%,#4d4a49)" role="img" aria-label="Photo of students in a lecture hall"></div>
</section>

<h2 class="abs title" style="left:0;top:3455px;width:1200px">Latest News</h2>
<div class="abs rule" style="top:3500px;left:520px;width:160px;height:1px"></div>

<article class="abs news" style="left:86px;top:3526px">
  <div class="date">JAN<b>24</b></div>
  <p>It is a long established fact is a long established fact</p>
  <div class="meta"><i>By Admin</i> - 08/05/2017 23 comments</div>
  <div class="more">READ MORE</div>
</article>
<article class="abs news" style="left:86px;top:3726px">
  <div class="date">JAN<b>26</b></div>
  <p>It is a long established fact is a long established fact</p>
  <div class="meta"><i>By Admin</i> - 08/05/2017 18 comments</div>
  <div class="more">READ MORE</div>
</article>
<article class="abs news right" style="left:878px;top:3526px">
  <div class="date">JAN<b>28</b></div>
  <p>It is a long established fact is a long established fact</p>
  <div class="meta"><i>By Admin</i> - 08/05/2017 16 comments</div>
  <div class="more">READ MORE</div>
</article>
<article class="abs news right" style="left:878px;top:3726px">
  <div class="date">JAN<b>15</b></div>
  <p>It is a long established fact is a long established fact</p>
  <div class="meta"><i>By Admin</i> - 08/05/2017 30 comments</div>
  <div class="more">READ MORE</div>
</article>
<div class="photo" style="left:344px;top:3526px;width:240px;height:172px;background:linear-gradient(180deg,#8b7a5c,#6f9a52)" role="img" aria-label="Photo of students gathered on a campus lawn"></div>
<div class="photo" style="left:608px;top:3526px;width:228px;height:172px;background:linear-gradient(180deg,#7a6650,#5a7c3c)" role="img" aria-label="Photo of students walking on campus"></div>
<div class="photo" style="left:344px;top:3726px;width:240px;height:172px;background:linear-gradient(180deg,#a0b07a,#5f8a3e)" role="img" aria-label="Photo of students studying outdoors"></div>
<div class="photo" style="left:608px;top:3726px;width:228px;height:172px;background:linear-gradient(180deg,#7f8c6a,#4f7a34)" role="img" aria-label="Photo of students sitting on grass"></div>

<section class="abs newsletter" role="img" aria-label="Background photo of a crowd of students">
  <div class="shade"></div>
  <h2 class="title" style="color:#fff;margin-top:102px;position:relative">Newsletter</h2>
  <div class="abs" style="left:540px;top:150px;width:120px;height:1px;background:#fff"></div>
  <div class="email-field">EMAIL</div>
  <div class="subscribe">SUBSCRIBE</div>
</section>

<section class="abs message">
  <div class="eyebrow">Get in touch</div>
  <h2>Send a Massege</h2>
  <div class="field">Name</div>
  <div class="field">Email</div>
  <div class="field">Massege</div>
</section>
<section class="abs info">
  <div class="eyebrow">Get in touch</div>
  <h2>Contact Information</h2>
  <div class="info-item">
    <svg width="20" height="26" viewBox="0 0 18 24"><path d="M9 1C4.6 1 1 4.5 1 8.9 1 15 9 23 9 23s8-8 8-14.1C17 4.5 13.4 1 9 1z" fill="none" stroke="#222" stroke-width="2"/><circle cx="9" cy="9" r="3" fill="#222"/></svg>
    <div><b>My Office</b><span>4/12 Larchwood</span></div>
  </div>
  <div class="info-item">
    <svg width="20" height="26" viewBox="0 0 18 24"><rect x="3" y="1" width="12" height="22" rx="2" fill="none" stroke="#222" stroke-width="2"/><circle cx="9" cy="19" r="1.5" fill="#222"/></svg>
    <div><b>My Mobile</b><span>0123 456 7890</span></div>
  </div>
  <div class="info-item">
    <svg width="22" height="18" viewBox="0 0 22 18"><rect x="1" y="1" width="20" height="16" fill="none" stroke="#222" stroke-width="2"/><path d="M1 1l10 9 10-9" fill="none" stroke="#222" stroke-width="2"/></svg>
    <div><b>My E-mail</b><span>hello@brightlantern.example</span></div>
  </div>
</section>
<div class="abs map" role="img" aria-label="Street map showing the office location"></div>

<footer class="abs footer">
  <div class="col" style="left:86px">
    <h5>Quick Menu</h5>
    <ul><li>Home</li><li>Students</li><li>School</li><li>Advisors</li><li>Member Resources</li><li>News</li><li>Contact Us</li></ul>
  </div>
  <div class="col" style="left:362px;width:210px">
    <h5>About Us</h5>
    <p>We connect home learners and other non-traditional students with college advisors and admissions officers in one friendly fair.</p>
  </div>
  <div class="col social" style="left:638px">
    <h5>Follow Us</h5>
    <ul><li><i></i>Newsfeed</li><li><i></i>Photo Wall</li><li><i></i>Video Channel</li></ul>
  </div>
  <div class="col" style="left:845px">
    <h5>Connect with us</h5>
    <p style="display:flex;gap:36px;font-weight:600"><span>Log in</span><span>Sign up</span></p>
  </div>
</footer>
<div class="abs copyright">COPYRIGHT THE BRIGHT LANTERN 2017 ALL RIGHT RESERVED</div>

</body>
</html>
```